VaultMeridan Business Card Re-Design

VaultMeridan is a specialized information security company that applies its proven methodology of security Assessment, Development, Integration and Training (A-D-I-T) to provide cyber security services in the areas of Data Protection, Network Defense and Compliance. We need the current business card re-designed to properly scale the fonts and possibly rearranging some elements (icons, lettering, etc.) to make the card more appealing to the eye. The card should have the logo that is on the web site (www.vaultmeridan-example.com). We would like ideas for both a black card (black background) and a white card (white background). We prefer rounded corners to help the card stand out but are open to all ideas. FYI: VaultMeridan's slogan is "...your security is our business".

Target Market(s)

#1 US Government Contracting Companies, #2 Commercial Companies, #3 Gen. Public.

Industry/Entity Type

Business

Contact Information for Business Card

See Description; open to the use of different fonts.

Font styles to use
Sans Serif

Colors
000000
ec1f27
ffffff

Requirements
Must have
• Company logo on web site, rounded corners, list of company offerings on the back of the card.
Nice to have
• Icons
Should not have
• none

```html
<!DOCTYPE html>
<html lang="en">
<head>
<meta charset="utf-8">
<title>VaultMeridan Business Card</title>
<link href="https://fonts.googleapis.com/css2?family=Dosis:wght@400;500;600;700&display=swap" rel="stylesheet">
<style>
  :root {
    --black: #000000;
    --red: #ec1f27;
    --white: #ffffff;
    --stage: #4e4e50;
    --muted: #6a6a6a;
  }
  * { margin: 0; padding: 0; box-sizing: border-box; }
  html, body { width: 1200px; height: 1000px; overflow: hidden; }
  body {
    background: var(--stage);
    font-family: "Dosis", sans-serif;
    position: relative;
  }
  .card {
    position: absolute;
    left: 276px;
    width: 646px;
    height: 363px;
    border-radius: 22px;
    background: var(--black);
    overflow: hidden;
  }
  .card--front { top: 130px; }
  .card--back { top: 540px; width: 644px; }

  /* front */
  .front-band {
    position: absolute; left: 0; right: 0; top: 116px; height: 140px;
    border-top: 4px solid var(--red);
    border-bottom: 4px solid var(--red);
    background: var(--white);
  }
  .front-band::before, .front-band::after {
    content: ""; position: absolute; left: 0; right: 0; height: 3px; background: var(--black);
  }
  .front-band::before { top: 0; }
  .front-band::after { bottom: 0; }
  .wordmark {
    position: absolute; left: 0; right: 0; text-align: center;
    display: flex; flex-direction: column; align-items: center;
  }
  .front-band .wordmark { top: 22px; }
  .wordmark__name {
    display: flex; align-items: center; gap: 14px;
    font-weight: 600; letter-spacing: 6px; text-transform: uppercase;
  }
  .wordmark__dot { width: 18px; height: 18px; background: var(--red); }
  .front-band .wordmark__name { font-size: 50px; color: var(--black); line-height: 1; }
  .wordmark__tag { font-weight: 500; text-transform: uppercase; letter-spacing: 1.5px; }
  .front-band .wordmark__tag { font-size: 24px; color: var(--black); margin-top: 10px; }

  /* back */
  .card--back .wordmark { top: 24px; }
  .card--back .wordmark__name { font-size: 30px; color: var(--white); gap: 10px; letter-spacing: 4px; line-height: 1; }
  .card--back .wordmark__dot { width: 12px; height: 12px; }
  .card--back .wordmark__tag { font-size: 14px; color: var(--white); margin-top: 6px; }

  .contact { position: absolute; left: 66px; top: 104px; color: var(--white); }
  .contact__name { font-size: 25px; font-weight: 600; letter-spacing: 0.5px; line-height: 1; }
  .contact__title { font-size: 15px; color: var(--red); font-weight: 500; margin-top: 4px; }
  .contact__lines { list-style: none; margin-top: 12px; }
  .contact__lines li { display: flex; align-items: center; gap: 9px; font-size: 16px; height: 20.3px; font-weight: 500; }
  .contact__lines svg { width: 14px; height: 14px; flex: none; }
  .contact__company { font-size: 14.5px; color: var(--red); margin-top: 10px; font-weight: 500; }
  .contact__address { font-size: 14.5px; font-weight: 500; line-height: 18px; }

  .divider {
    position: absolute; left: 321px; top: 104px; height: 222px;
    border-left: 1px dashed var(--muted);
  }
  .services {
    position: absolute; left: 338px; top: 103px; list-style: none;
    color: var(--white); font-size: 15px; font-weight: 500;
  }
  .services li { height: 20px; line-height: 20px; display: flex; align-items: center; }
  .services li::before {
    content: ""; width: 4px; height: 4px; border-radius: 50%; background: var(--red); margin-right: 6px;
  }
  .back-footer {
    position: absolute; left: 0; right: 0; bottom: 0; height: 20px;
    border-top: 3px solid var(--red); background: var(--white);
  }
  .back-footer::before {
    content: ""; position: absolute; left: 0; right: 0; top: 0; height: 3px; background: var(--black);
  }
</style>
</head>
<body>

<section class="card card--front" aria-label="Card front">
  <div class="front-band">
    <div class="wordmark">
      <div class="wordmark__name"><span class="wordmark__dot"></span>VaultMeridan</div>
      <div class="wordmark__tag">Information Security</div>
    </div>
  </div>
</section>

<section class="card card--back" aria-label="Card back">
  <div class="wordmark">
    <div class="wordmark__name"><span class="wordmark__dot"></span>VaultMeridan</div>
    <div class="wordmark__tag">Information Security</div>
  </div>

  <div class="contact">
    <div class="contact__name">MARCUS BELL</div>
    <div class="contact__title">President / CEO</div>
    <ul class="contact__lines">
      <li><svg viewBox="0 0 14 14"><path d="M1 5 Q7 0 13 5 L11 6.5 L9.5 4.5 L4.5 4.5 L3 6.5 Z M3 8 L11 8 L12 13 L2 13 Z" fill="#ec1f27"/><circle cx="7" cy="10.5" r="1.5" fill="#000"/></svg>240.555.0142</li>
      <li><svg viewBox="0 0 14 14"><rect x="3.5" y="1" width="7" height="12" rx="1.2" fill="none" stroke="#ec1f27" stroke-width="1.6"/><rect x="6" y="10.5" width="2" height="1" fill="#ec1f27"/></svg>301.555.0187</li>
      <li><svg viewBox="0 0 14 14" fill="none" stroke="#ec1f27" stroke-width="1.2"><circle cx="7" cy="7" r="5.8"/><ellipse cx="7" cy="7" rx="2.6" ry="5.8"/><path d="M1.2 7 H12.8 M2 4 H12 M2 10 H12"/></svg>www.vaultmeridan-example.com</li>
      <li><svg viewBox="0 0 14 14"><rect x="1" y="3" width="12" height="9" fill="#ec1f27"/><path d="M1.5 3.5 L7 8 L12.5 3.5 M1.5 11.5 L5.5 7 M12.5 11.5 L8.5 7" stroke="#000" stroke-width="1" fill="none"/></svg>info@vaultmeridan-example.com</li>
      <li><svg viewBox="0 0 14 14"><rect x="1" y="3" width="12" height="9" fill="#ec1f27"/><path d="M1.5 3.5 L7 8 L12.5 3.5 M1.5 11.5 L5.5 7 M12.5 11.5 L8.5 7" stroke="#000" stroke-width="1" fill="none"/></svg>mbell@vaultmeridan-example.com</li>
    </ul>
    <div class="contact__company">VaultMeridan, Inc.</div>
    <div class="contact__address">4120 Harbor Ridge Rd. Suite 210,<br>Columbia, Maryland 21046</div>
  </div>

  <div class="divider"></div>

  <ul class="services">
    <li>Secure Could &amp; Open Stack Solutions</li>
    <li>Network Attack Penetration &amp; Defense</li>
    <li>Red/Blue Team</li>
    <li>Data Center Consolidation</li>
    <li>Secure Virtual Computing</li>
    <li>Classified Cross Domain Solutions</li>
    <li>Foreign/Counter Intelligence Data Security</li>
    <li>Training Assessment &amp; Integration</li>
    <li>Security Subject Matter Experts</li>
    <li>Executive Security Strategy Coaching</li>
    <li>Data Encryption/Privacy</li>
  </ul>

  <div class="back-footer"></div>
</section>

</body>
</html>
```